AUSTRALIAN CONSULTING FIRM BUSINESS CARD - MODERN

We are wanting a modern, clean lined business card design. We are professional niche consultancy firm situated in Australia called Marlow Advisory Partners Pty Ltd.
The card should communicate professionalism and creativity and draw on our logo design (attached).
The design should be two sided, landscape orientation.
Target Market(s)
government, not for profit sector, corporate clients
Industry/Entity Type
Landscape
Requirements
Must have
- logo
no new introduced colours

```html
<!DOCTYPE html>
<html lang="en">
<head>
<meta charset="utf-8">
<title>Marlow Advisory Partners – Business Card</title>
<link rel="stylesheet" href="https://fonts.googleapis.com/css2?family=Open+Sans:wght@400;600;700&display=swap">
<style>
  :root {
    --backdrop: #e9e9ec;
    --card-white: #ffffff;
    --card-shade: #ececee;
    --brand-navy: #1d4aa8;
    --brand-sky: #1ea2e2;
    --text-dark: #333a44;
    --text-body: #3e4550;
  }
  * { margin: 0; padding: 0; box-sizing: border-box; }
  html, body {
    width: 1200px; height: 646px; overflow: hidden;
    background: var(--backdrop);
    font-family: "Open Sans", Arial, sans-serif;
  }
  .canvas {
    position: relative; width: 1200px; height: 646px;
    display: flex; align-items: center; justify-content: center; gap: 60px;
  }
  .card {
    position: relative; width: 510px; height: 292px; overflow: hidden;
    background: radial-gradient(ellipse at 45% 35%, var(--card-white) 40%, var(--card-shade) 100%);
    box-shadow: 0 6px 18px rgba(0,0,0,.18);
  }
  /* contact side */
  .card-contact .brand-mark {
    position: absolute; top: 22px; right: 24px;
    display: flex; align-items: center; gap: 6px;
    font-size: 11px; font-weight: 700; color: var(--brand-navy);
  }
  .brand-dot {
    width: 12px; height: 12px; border-radius: 50%; background: var(--brand-navy);
  }
  .contact-name {
    position: absolute; left: 40px; top: 120px;
    font-size: 24px; font-weight: 600; color: var(--brand-sky);
  }
  .contact-role {
    font-size: 14px; font-weight: 400; color: var(--text-dark); margin-left: 4px;
  }
  .contact-list {
    position: absolute; left: 40px; top: 166px; list-style: none;
  }
  .contact-list li {
    display: flex; align-items: center; gap: 10px;
    height: 24px; margin-bottom: 3px;
    font-size: 12.5px; color: var(--text-body);
  }
  .contact-icon {
    width: 20px; height: 20px; border-radius: 3px; background: var(--brand-sky);
    display: flex; align-items: center; justify-content: center;
  }
  /* logo side */
  .card-logo .brand-lockup {
    position: absolute; left: 0; right: 0; top: 100px;
    display: flex; align-items: center; justify-content: center; gap: 12px;
  }
  .brand-lockup .brand-dot { width: 30px; height: 30px; }
  .brand-lockup .brand-name {
    font-size: 22px; font-weight: 700; color: var(--brand-navy);
  }
  .card-band {
    position: absolute; left: 0; right: 0; bottom: 0; height: 22px;
    background: var(--brand-navy);
  }
</style>
</head>
<body>
<main class="canvas">
  <section class="card card-contact" aria-label="Card back with contact details">
    <div class="brand-mark"><span class="brand-dot"></span>Marlow Advisory Partners Pty Ltd</div>
    <h1 class="contact-name">Clara Whitfield<span class="contact-role">Director</span></h1>
    <ul class="contact-list">
      <li>
        <span class="contact-icon"><svg width="12" height="12" viewBox="0 0 24 24"><path fill="#fff" d="M6.6 10.8a15 15 0 0 0 6.6 6.6l2.2-2.2c.3-.3.7-.4 1-.2 1.1.4 2.3.6 3.6.6.6 0 1 .4 1 1V20c0 .6-.4 1-1 1A17 17 0 0 1 3 4c0-.6.4-1 1-1h3.5c.6 0 1 .4 1 1 0 1.3.2 2.5.6 3.6.1.3 0 .7-.2 1z"/></svg></span>
        0321 555 0148
      </li>
      <li>
        <span class="contact-icon"><svg width="12" height="12" viewBox="0 0 24 24"><rect x="2" y="5" width="20" height="14" rx="2" fill="#fff"/><path d="M3 6l9 7 9-7" fill="none" stroke="#1ea2e2" stroke-width="2"/></svg></span>
        clara@marlowadvisory.com
      </li>
      <li>
        <span class="contact-icon"><svg width="12" height="12" viewBox="0 0 24 24" fill="none" stroke="#fff" stroke-width="2"><circle cx="12" cy="12" r="9"/><path d="M3 12h18M12 3c3 3 3 15 0 18M12 3c-3 3-3 15 0 18"/></svg></span>
        www.marlowadvisory.com
      </li>
      <li>
        <span class="contact-icon"><svg width="12" height="12" viewBox="0 0 24 24"><path fill="#fff" d="M12 2a7 7 0 0 0-7 7c0 5 7 13 7 13s7-8 7-13a7 7 0 0 0-7-7zm0 9.5A2.5 2.5 0 1 1 12 6.5a2.5 2.5 0 0 1 0 5z"/></svg></span>
        4/12 Hartley rd, Kensington. 2033
      </li>
    </ul>
  </section>

  <section class="card card-logo" aria-label="Card front with company name">
    <div class="brand-lockup">
      <span class="brand-dot"></span>
      <span class="brand-name">Marlow Advisory Partners Pty Ltd</span>
    </div>
    <div class="card-band"></div>
  </section>
</main>
</body>
</html>
```